Lotus Depot Community Wordpress Site

Branding package: http://www.lotusdepot.example/drop/Lotus_Depot_Branding_v02.pdf
**please reference above branding package when creating theme.
The goal is to have the site come off industrious and functional. A warehouse feel without being too cold.
We are looking for a theme/skin for our wordpress site. The blog has already been setup and all necessary plugins have been installed.
Lotus Depot is the local yoga enthusiasts online portal for information regarding yoga in the community. It is a place to share experiences, events, knowledge, and encouragement, ultimately serving to build community and connect people in their love for the practice of yoga.
Work with the concept of a warehouse, it is a warehouse of ideas.
Some keywords that describe the site:
Energetic, friendly, welcoming, industrious, fun, confident, charming, grounded, functional.
Color Palette: http://www.lotusdepot.example/drop/color-palette.png
Logo: http://www.lotusdepot.example/drop/logo.png
Target Market(s)
Predominantly women, mid 20s to mid 40s however appeals to anyone one looking for yoga in the area and while its predominantly females the site should have a masculine look.
Industry/Entity Type
Events
Requirements
Must have
- Must use the color palette
Must use provided logo
Should not have
- plain white background.

```html
<!DOCTYPE html>
<html lang="en">
<head>
<meta charset="utf-8">
<title>Lotus Depot</title>
<link rel="stylesheet" href="https://fonts.googleapis.com/css2?family=Lato:wght@300;400;700&family=Roboto+Condensed:wght@400;700&family=Arimo:wght@400;700&display=swap">
<style>
  :root {
    --purple: #7b1f6f;
    --purple-dark: #5e1554;
    --sky: #5ea9de;
    --sky-soft: #cfe6f4;
    --nav-grey: #a7adb3;
    --nav-grey-dark: #8f959b;
    --ink: #222;
    --ink-soft: #444;
    --btn-dark: #4a4a4a;
    --panel-blue: #4f6d85;
    --panel-field: #2c3338;
    --footer: #283a47;
    --footer-muted: #6b7d8a;
    --rule: #ececec;
  }
  * { box-sizing: border-box; margin: 0; padding: 0; }
  html, body { width: 1200px; height: 788px; overflow: hidden; }
  body {
    position: relative;
    font-family: "Arimo", Arial, sans-serif;
    color: var(--ink);
    background: #fff;
  }
  .sky-wash {
    position: absolute; left: 0; top: 0; width: 1200px; height: 150px;
    background: linear-gradient(180deg, var(--sky-soft) 0%, #eaf4fa 55%, #fff 100%);
  }
  .ground-wash {
    position: absolute; left: 0; top: 560px; width: 1200px; height: 160px;
    background: linear-gradient(180deg, #fff 0%, #eef0f2 50%, #dfe3e6 100%);
  }
  .brand {
    position: absolute; left: 197px; top: 18px;
    display: flex; align-items: center; gap: 8px;
    font-family: "Lato", sans-serif; font-weight: 700; font-size: 34px;
    color: var(--purple); letter-spacing: -0.5px;
  }
  .brand-dot { width: 14px; height: 14px; border-radius: 50%; background: var(--purple); }
  .social { position: absolute; left: 902px; top: 12px; display: flex; gap: 9px; }
  .social span { width: 28px; height: 30px; border-radius: 5px; display: block; }
  .social .s1 { background: #3cb5e8; }
  .social .s2 { background: #3b5998; }
  .social .s3 { background: #d5312b; }

  .main-nav {
    position: absolute; left: 188px; top: 95px; width: 823px; height: 38px;
    background: linear-gradient(180deg, var(--nav-grey) 0%, var(--nav-grey-dark) 100%);
    border-radius: 4px;
  }
  .main-nav a {
    position: absolute; top: 13px; color: #fff; text-decoration: none;
    font-family: "Arimo", sans-serif; font-size: 12.5px;
  }
  .main-nav .active {
    top: -10px; left: 11px; width: 85px; height: 48px;
    background: var(--purple); border-bottom: 3px solid #3d0d37;
    text-align: center; padding-top: 23px;
  }
  .member-login {
    position: absolute; left: 867px; top: 89px; width: 121px; height: 47px;
    background: linear-gradient(180deg, #8e2a82, var(--purple-dark));
    border-radius: 4px; color: #fff; text-align: center; line-height: 47px;
    font-family: "Roboto Condensed", sans-serif; font-weight: 700; font-size: 17px;
    box-shadow: 0 2px 3px rgba(0,0,0,.25);
  }

  .hero-photo {
    position: absolute; left: 215px; top: 145px; width: 254px; height: 275px;
    background: radial-gradient(ellipse at 50% 55%, #f2f2f2 0%, #fafafa 60%, #fff 100%);
  }
  .slider-dots { position: absolute; left: 330px; top: 422px; display: flex; gap: 4px; }
  .slider-dots span { width: 11px; height: 11px; border-radius: 50%; background: #b9c3cb; }
  .slider-dots .on { background: var(--purple); }

  .hero-kicker {
    position: absolute; left: 580px; top: 168px;
    font-family: "Lato", sans-serif; font-weight: 300; font-size: 44px; color: var(--sky);
  }
  .hero-title {
    position: absolute; left: 582px; top: 224px;
    font-family: "Roboto Condensed", sans-serif; font-weight: 700; font-size: 32px; color: var(--sky);
  }
  .hero-copy {
    position: absolute; left: 584px; top: 276px; width: 400px;
    font-size: 11px; line-height: 18.4px; color: var(--ink);
  }
  .btn {
    position: absolute; display: block; color: #fff; text-align: center;
    font-family: "Roboto Condensed", sans-serif;
    background: linear-gradient(180deg, #6c6c6c, var(--btn-dark) 55%, #3a3a3a);
    border: 1px solid #2e2e2e; border-radius: 4px;
    box-shadow: 0 3px 0 #bcbcbc, 0 4px 4px rgba(0,0,0,.3);
  }
  .btn-join { left: 584px; top: 349px; width: 190px; height: 47px; line-height: 45px; font-size: 22px; font-weight: 700; }
  .btn-small { width: 87px; height: 31px; line-height: 29px; font-size: 14.5px; }

  .rule { position: absolute; left: 0; top: 439px; width: 1200px; height: 5px; background: var(--rule); }

  .col-title {
    position: absolute; top: 456px;
    font-family: "Lato", sans-serif; font-weight: 300; font-size: 28px; color: var(--purple-dark);
  }
  .welcome-lead {
    position: absolute; left: 193px; top: 500px; width: 225px;
    font-size: 11px; line-height: 17.3px; font-weight: 700; color: var(--sky);
  }
  .welcome-body {
    position: absolute; left: 193px; top: 561px; width: 225px;
    font-size: 11px; line-height: 17.3px; color: var(--ink-soft);
  }
  .news { position: absolute; left: 493px; width: 230px; font-size: 11px; line-height: 17.3px; color: var(--ink-soft); }
  .news time { display: block; font-family: "Roboto Condensed", sans-serif; font-weight: 700; color: #8b8b8b; font-size: 12px; }
  .news b { color: var(--ink); }

  .contact-card {
    position: absolute; left: 795px; top: 463px; width: 193px; height: 217px;
    background: var(--panel-blue); border-radius: 6px;
  }
  .contact-inner {
    position: absolute; left: 11px; top: 52px; width: 171px; height: 157px;
    border: 1px dashed #7e98ac; border-radius: 3px;
  }
  .field {
    position: absolute; left: 10px; width: 150px; height: 20px;
    background: var(--panel-field); border: 1px solid #1d2226; border-radius: 2px;
    color: #8a9299; font-size: 6.5px; padding: 6px 0 0 19px;
  }
  .field svg { position: absolute; left: 6px; top: 5px; }
  .send {
    position: absolute; left: 101px; top: 121px; width: 66px; height: 19px;
    background: linear-gradient(180deg, #f4f4f4, #c9c9c9); border-radius: 10px;
    font-size: 7.5px; font-weight: 700; color: #333; text-align: center; line-height: 19px;
  }
  .ribbon { position: absolute; left: 769px; top: 476px; }

  .site-footer {
    position: absolute; left: 0; top: 718px; width: 1200px; height: 70px; background: var(--footer);
  }
  .footer-links {
    position: absolute; left: 0; top: 23px; width: 1200px; text-align: center;
    color: #fff; font-size: 11px; word-spacing: 1px;
  }
  .footer-links span { margin: 0 7px; }
  .copyright {
    position: absolute; left: 0; top: 46px; width: 1200px; text-align: center;
    color: var(--footer-muted); font-size: 10.5px;
  }
</style>
</head>
<body>
  <div class="sky-wash"></div>
  <div class="ground-wash"></div>

  <header>
    <div class="brand"><span class="brand-dot"></span>Lotus Depot</div>
    <div class="social" aria-label="Social links"><span class="s1"></span><span class="s2"></span><span class="s3"></span></div>
    <nav class="main-nav">
      <a class="active" style="left:11px">Welcome</a>
      <a style="left:125px">Wellness</a>
      <a style="left:221px">Program &amp; Workshops</a>
      <a style="left:388px">Blog</a>
      <a style="left:459px">Events</a>
      <a style="left:542px">Connect People</a>
    </nav>
    <a class="member-login">Member Login</a>
  </header>

  <section class="hero">
    <div class="hero-photo" role="img" aria-label="Photo of a woman in white holding a seated yoga pose"></div>
    <div class="slider-dots"><span class="on"></span><span></span><span></span><span></span></div>
    <p class="hero-kicker">Enter to win a yoga</p>
    <h1 class="hero-title">RETREAT TO CORAL COVE</h1>
    <p class="hero-copy">This November 17 - 24th, 2012, join us for seven days &amp; nights surrounded by pristine Caribbean beaches &amp; healthy, fresh meals as four of our amazing teachers lead five yoga classes of various styles every day!</p>
    <a class="btn btn-join">Join Our Community</a>
  </section>

  <div class="rule"></div>

  <section>
    <h2 class="col-title" style="left:192px">Welcome!</h2>
    <p class="welcome-lead">Lorem ipsum dolor sit amet, consectetur in tempus mi condimentum eget. Fuscesapielit tortorLorem</p>
    <p class="welcome-body">Lorem ipsum dolor sit amet, consectetur in tempus mi condimentum eget. Fuscesapielit tortorLorem ipsum dolor sit amet, consectetu-rin tempus Lorem ipsum dolor sit amet,</p>
    <a class="btn btn-small" style="left:193px;top:644px">Know More</a>
  </section>

  <section>
    <h2 class="col-title" style="left:492px">News &amp; Event</h2>
    <div class="news" style="top:501px"><time>15/5/2012</time><b>Lorem ipsum dolor sit amet,</b> consectetur in tempus mi condimentum eget. Fuscesapielit</div>
    <div class="news" style="top:563px"><time>15/5/2012</time><b>Lorem ipsum dolor sit amet,</b> consectetur in tempus mi condimentum eget. Fuscesapielit tortorLorem ipsum dolor sit amet, consect</div>
    <a class="btn btn-small" style="left:493px;top:644px">More News</a>
  </section>

  <aside class="contact-card">
    <div class="contact-inner">
      <div class="field" style="top:12px"><svg width="8" height="8" viewBox="0 0 8 8"><circle cx="4" cy="2.3" r="2" fill="#8a9299"/><path d="M0 8c0-3 8-3 8 0z" fill="#8a9299"/></svg>Name</div>
      <div class="field" style="top:40px"><svg width="9" height="7" viewBox="0 0 9 7"><rect x=".5" y=".5" width="8" height="6" fill="none" stroke="#8a9299"/><path d="M.5.5 4.5 4 8.5.5" fill="none" stroke="#8a9299"/></svg>Mail ID</div>
      <div class="field" style="top:68px;height:48px"><svg width="8" height="8" viewBox="0 0 8 8"><path d="M1 7 6 2l1 1-5 5H1z" fill="#8a9299"/></svg>Message</div>
      <div class="send">SEND QUERY</div>
    </div>
  </aside>
  <svg class="ribbon" width="242" height="36" viewBox="0 0 242 36" aria-hidden="true">
    <path d="M0 8h22v28H6l6-14z" fill="#9aa6ae"/>
    <path d="M242 8h-22v28h16l-6-14z" fill="#9aa6ae"/>
    <rect x="18" y="0" width="206" height="32" fill="#c7cdd1"/>
    <rect x="18" y="0" width="206" height="16" fill="#d6dbde"/>
    <line x1="28" y1="16" x2="72" y2="16" stroke="#8d979d"/>
    <line x1="170" y1="16" x2="214" y2="16" stroke="#8d979d"/>
    <circle cx="76" cy="16" r="2.5" fill="#777"/><circle cx="166" cy="16" r="2.5" fill="#777"/>
    <text x="121" y="22" text-anchor="middle" font-family="Roboto Condensed, sans-serif" font-size="17" fill="#3a3f44">Contact Us</text>
  </svg>

  <footer class="site-footer">
    <p class="footer-links">Welcome<span>|</span>Wellness<span>|</span>Program &amp; Workshops<span>|</span>Blog<span>|</span>Events<span>|</span>Connect People</p>
    <p class="copyright">All rights reserved by lotusdepot pvt.ltd</p>
  </footer>
</body>
</html>
```